Re-Design Korbalex.com make it more professional looking

We want to re-design this website, we are currently not happy with existing design. Some of the design examples are listed below.

https://trelvan.com/
https://www.quostel.com/
https://www.namity.com/projects/
https://www.flarnside.com/

The content on the website is final, there will be no change in the content. We just need to re-design the site. Features page on the site is very important and need to be layout very well.

Industry/Entity Type

It Professional

Number of Pages Required

4 page

Font styles to use
Sans Serif

Requirements
Must have
• Professional look and design like the examples i quoted above and a nice color theme. I do not have preferences but i like the quostel.com and trelvan.com

```html
<!DOCTYPE html>
<html lang="en">
<head>
<meta charset="utf-8">
<title>Korbalex — Online SEO Project Management</title>
<link rel="stylesheet" href="https://fonts.googleapis.com/css2?family=Open+Sans:wght@400;600;700&display=swap">
<style>
:root{
  --orange:#f7941d;
  --orange-dark:#e07f0a;
  --ink:#1e1e1e;
  --text:#4a4a4a;
  --muted:#8a8a8a;
  --light:#f2f2f2;
  --white:#ffffff;
  --dark:#1c1c1c;
  --darker:#141414;
  --blue:#2aa9e0;
}
*{box-sizing:border-box;margin:0;padding:0}
html,body{width:1200px;height:3789px;overflow:hidden}
body{font-family:"Open Sans",Arial,sans-serif;color:var(--text);background:var(--white);position:relative}
.section{position:absolute;left:0;width:1200px;overflow:hidden}
.abs{position:absolute}
.btn{position:absolute;display:flex;align-items:center;justify-content:center;background:var(--orange);color:var(--white);font-size:15px;font-weight:600;border-radius:2px}
.hl{color:var(--orange)}
.body-text{font-size:15.5px;line-height:27px;color:var(--text)}
h2.title{font-weight:600;color:var(--ink);font-size:33px;line-height:1.2}

/* hero */
.hero{top:0;height:687px;background:linear-gradient(120deg,#3d4047 0%,#6a6d72 40%,#9a9ca0 70%,#55585e 100%)}
.hero-shade{position:absolute;inset:0;background:rgba(20,20,25,.35)}
.nav{position:absolute;top:0;left:0;width:1200px;height:101px;background:rgba(20,20,25,.45);border-bottom:1px solid rgba(255,255,255,.15)}
.logo{position:absolute;left:28px;top:28px;display:flex;align-items:center;gap:12px;color:var(--white);font-size:34px;font-weight:700}
.logo-dot{width:30px;height:30px;border-radius:50%;background:var(--orange)}
.nav-link{position:absolute;top:0;height:101px;display:flex;align-items:center;color:var(--white);font-size:14px;font-weight:600;letter-spacing:.5px}
.nav-link.active{background:var(--orange);justify-content:center;width:71px}
.login{top:30px;left:1038px;width:111px;height:41px;font-size:14px}
.hero h1{position:absolute;top:285px;width:100%;text-align:center;color:var(--white);font-size:62px;font-weight:600;letter-spacing:-.5px}
.hero-sub{position:absolute;top:378px;width:100%;text-align:center;color:var(--white);font-size:23px}
.hero-cta{left:475px;top:455px;width:252px;height:60px;background:var(--blue);font-size:18px;font-weight:600}
.dots{position:absolute;top:636px;left:583px;display:flex;gap:10px}
.dots span{width:15px;height:15px;border-radius:50%;border:2px solid var(--white)}
.dots span.on{background:var(--white)}

/* welcome */
.welcome{top:687px;height:280px;background:var(--white)}
.welcome-title{position:absolute;top:45px;width:100%;text-align:center;font-size:35px;font-weight:600;color:var(--ink)}
.rule{position:absolute;top:68px;height:1px;width:220px;background:#d5d5d5}
.welcome-text{position:absolute;left:100px;top:112px;width:1000px;text-align:center;font-size:12.5px;line-height:21px;color:var(--muted)}
.welcome .btn{left:528px;top:192px;width:144px;height:46px;font-size:13px}

/* feature rows */
.feature{height:354px}
.gray{background:var(--light)}
.art{position:absolute;border-radius:4px}
.feat-title{position:absolute;font-size:33px;font-weight:600;color:var(--ink)}
.feat-text{position:absolute}
.feat-btn{width:245px;height:37px;font-size:13px}

/* integrations */
.integrations{top:1698px;height:368px;background:linear-gradient(180deg,#222 0%,#161616 100%)}
.int-title{position:absolute;top:54px;width:100%;text-align:center;color:var(--white);font-size:30px;font-weight:600}
.app{position:absolute;top:134px;width:160px;text-align:center;color:var(--white);font-size:20px}
.app svg{display:block;margin:0 auto 18px}

/* testimonials */
.testimonials{top:2837px;height:333px;background:#ededed}
.quote-box{position:absolute;left:374px;top:113px;width:429px;height:172px;background:var(--white);padding:40px 30px 0 30px;font-size:12.5px;line-height:21px;color:var(--muted);font-style:italic}
.qmark{position:absolute;color:var(--orange);font-size:70px;font-weight:700;line-height:1}
.avatar{position:absolute;left:834px;top:124px;width:80px;height:80px;border-radius:50%;background:linear-gradient(180deg,#c9c9c9,#8e8e8e);border:3px solid var(--white)}
.person{position:absolute;left:800px;top:208px;width:148px;text-align:center}
.person b{display:block;color:var(--orange);font-size:19px;font-weight:600}
.person span{font-size:12px;color:var(--muted)}

/* newsletter + footer */
.footer{top:3170px;height:619px;background:linear-gradient(160deg,#2a2c30 0%,#1a1b1e 60%,#121214 100%)}
.news-title{position:absolute;top:45px;width:100%;text-align:center;color:var(--white);font-size:33px;letter-spacing:1px}
.news-form{position:absolute;left:265px;top:121px;width:745px;height:69px;background:rgba(120,120,120,.55)}
.news-input{position:absolute;left:65px;top:0;height:69px;display:flex;align-items:center;color:#e6e6e6;font-size:22px}
.subscribe{left:546px;top:14px;width:184px;height:40px;font-size:15px;font-weight:700}
.col{position:absolute;top:298px;width:240px}
.col h4{color:var(--orange);font-size:16px;font-weight:600;padding-bottom:12px;border-bottom:1px dashed #666;width:190px}
.col ul{list-style:none;margin-top:20px}
.col li{color:#e0e0e0;font-size:13px;line-height:31px}
.col li::before{content:"•";margin-right:10px;color:#e0e0e0}
.contact li::before{content:none}
.contact li{display:flex;gap:14px;align-items:flex-start;line-height:19px;margin-bottom:10px}
.bottom{position:absolute;top:548px;left:0;width:1200px;height:1px;background:rgba(255,255,255,.15)}
.copy{position:absolute;top:575px;left:45px;color:#cfcfcf;font-size:12.5px}
.social{position:absolute;top:572px;left:990px;display:flex;gap:22px}
.social span{width:16px;height:16px;border-radius:50%;background:#8a8a8a}
.social span.first{background:var(--orange)}
</style>
</head>
<body>

<!-- hero -->
<section class="section hero">
  <div class="abs" role="img" aria-label="Business people shaking hands over a desk with a tablet" style="inset:0"></div>
  <div class="hero-shade"></div>
  <nav class="nav">
    <div class="logo"><span class="logo-dot"></span>Korbalex</div>
    <a class="nav-link active" style="left:308px">HOME</a>
    <a class="nav-link" style="left:425px">FEATURES</a>
    <a class="nav-link" style="left:548px">PRICING</a>
    <a class="nav-link" style="left:660px">ABOUT US</a>
    <a class="nav-link" style="left:786px">CONTACT US</a>
    <a class="btn login">LOGIN</a>
  </nav>
  <h1>Online SEO Project Management</h1>
  <p class="hero-sub">Share your experience with us and get 3 months of premium access for free</p>
  <a class="btn hero-cta">GET STARTED NOW</a>
  <div class="dots"><span class="on"></span><span></span><span></span></div>
</section>

<!-- welcome -->
<section class="section welcome">
  <div class="rule" style="left:105px"></div>
  <div class="rule" style="left:875px"></div>
  <h2 class="welcome-title">Welcome to <span class="hl">Korbalex</span></h2>
  <p class="welcome-text">Lorem ipsum dolor sit amet, consectetur adipisicing elit, sed do eiusmod tempor incididunt ut labore et dolore magna aliqua. Ut enim ad minim veniam, quis nostrud exercitation ullamco laboris nisi ut aliquip ex ea commodo consequat. Duis aute irure dolor in reprehenderit in voluptate velit esse cillum dolore eu fugiat nulla pariatur. Excepteur sint occaecat cupidatat non proident, sunt in culpa qui officia deserunt mollit anim id est laborum.</p>
  <a class="btn">READ MORE</a>
</section>

<!-- organize, collaborate -->
<section class="section feature gray" style="top:967px">
  <div class="art" role="img" aria-label="Illustration of a team meeting around a whiteboard with role labels" style="left:10px;top:18px;width:394px;height:316px;background:linear-gradient(160deg,#dfe6ec,#b9c4cc)"></div>
  <h2 class="feat-title" style="left:424px;top:75px">Organize, <span class="hl">Collaborate and Deliver</span></h2>
  <p class="feat-text body-text" style="left:424px;top:130px;width:740px;font-size:14px;line-height:23px">Being an SEO agency we did not find any tool that can help agencies to manage an SEO project lifecycle effectively. That is why we decided to bring Korbalex "A robust SEO project management tool" for SEO Agencies to provide them the solution to manage their projects in an organized way.</p>
  <a class="btn feat-btn" style="left:424px;top:253px">Features for Digital Agencies</a>
</section>

<!-- best project management -->
<section class="section feature" style="top:1321px;height:377px">
  <div class="art" role="img" aria-label="Laptop and phone showing the project dashboard" style="left:859px;top:81px;width:328px;height:215px;background:linear-gradient(160deg,#e9ecef,#9aa3ab)"></div>
  <h2 class="feat-title" style="left:40px;top:123px">Best Project <span class="hl">Management Tool for Digital Agencies</span></h2>
  <p class="feat-text body-text" style="left:45px;top:174px;width:790px;font-size:14px;line-height:23px">Now SEO management is not at all a hectic task. Organize your SEO projects more effectively &amp; efficiently. Korbalex helps you to track every pitfall to projects and to find out their solutions on time. Give a powerful tool to your team to schedule their priorities &amp; finish things on time. Korbalex guides you to do the right things than to do things right. It's the most effective online tool that makes tasks easy and extremely manageable.</p>
  <a class="btn feat-btn" style="left:45px;top:296px">Features for Digital Agencies</a>
</section>

<!-- integrations -->
<section class="section integrations">
  <h2 class="int-title">Integrated with some of the most popular apps you already love</h2>
  <div class="app" style="left:59px"><svg width="106" height="106"><circle cx="53" cy="53" r="53" fill="#f7941d"/><circle cx="53" cy="53" r="34" fill="none" stroke="#fff" stroke-width="4"/></svg>Integrated</div>
  <div class="app" style="left:246px"><svg width="106" height="106"><circle cx="53" cy="53" r="53" fill="#f7941d"/><circle cx="53" cy="53" r="34" fill="none" stroke="#fff" stroke-width="4"/></svg>Integrated</div>
  <div class="app" style="left:430px"><svg width="106" height="106"><circle cx="53" cy="53" r="53" fill="#f7941d"/><circle cx="53" cy="53" r="34" fill="none" stroke="#fff" stroke-width="4"/></svg>Integrated</div>
  <div class="app" style="left:620px"><svg width="106" height="106"><circle cx="53" cy="53" r="53" fill="#f7941d"/><circle cx="53" cy="53" r="34" fill="none" stroke="#fff" stroke-width="4"/></svg>Coming Soon</div>
  <div class="app" style="left:804px"><svg width="106" height="106"><circle cx="53" cy="53" r="53" fill="#f7941d"/><circle cx="53" cy="53" r="34" fill="none" stroke="#fff" stroke-width="4"/></svg>Coming Soon</div>
  <div class="app" style="left:994px"><svg width="106" height="106"><circle cx="53" cy="53" r="53" fill="#f7941d"/><circle cx="53" cy="53" r="34" fill="none" stroke="#fff" stroke-width="4"/></svg>Coming Soon</div>
</section>

<!-- stress -->
<section class="section feature gray" style="top:2066px;height:359px">
  <div class="art" role="img" aria-label="Overhead illustration of a team working around a table" style="left:0;top:18px;width:417px;height:328px;background:linear-gradient(160deg,#e4e2dc,#b8b3a8)"></div>
  <h2 class="feat-title" style="left:460px;top:83px">Stress! <span class="hl">Take it out of your projects</span></h2>
  <p class="feat-text body-text" style="left:460px;top:148px;width:700px;font-size:14px;line-height:23px">Korbalex allows you to manage people, time and resources to properly implement an easy and stress-free project management process. Using Korbalex, you can easily identify what could slow down your projects progress in future, and it enables you to take corrective actions in advance.</p>
  <a class="btn feat-btn" style="left:460px;top:248px">Features for Digital Agencies</a>
</section>

<!-- organize and get it done -->
<section class="section feature" style="top:2425px;height:412px">
  <div class="art" role="img" aria-label="Laptop, tablet and phone showing the task manager" style="left:859px;top:38px;width:341px;height:341px;background:linear-gradient(160deg,#eef0f2,#a4abb2)"></div>
  <h2 class="feat-title" style="left:48px;top:80px">Organize <span class="hl">and Get it Done</span></h2>
  <p class="feat-text body-text" style="left:48px;top:139px;width:790px;font-size:14px;line-height:23px">Korbalex grants you access to measure every important aspect related to your projects effectively from a place. We believe what you measure you can manage. It's specifically designed for SEO project management keeping all project management needs in mind. You will get detailed Information related to your projects online which will help you to get rid of offline management tools.</p>
  <a class="btn feat-btn" style="left:45px;top:263px">Features for Digital Agencies</a>
</section>

<!-- testimonials -->
<section class="section testimonials">
  <h2 class="abs" style="top:35px;width:100%;text-align:center;font-size:33px;font-weight:600;color:var(--ink)">Our <span class="hl">Testimonials</span></h2>
  <svg class="abs" style="left:205px;top:146px" width="44" height="110"><polyline points="40,2 4,55 40,108" fill="none" stroke="#c4c4c4" stroke-width="2"/></svg>
  <svg class="abs" style="left:1010px;top:146px" width="44" height="110"><polyline points="4,2 40,55 4,108" fill="none" stroke="#c4c4c4" stroke-width="2"/></svg>
  <div class="quote-box">Lorem ipsum dolor sit amet, consectetur adipiscing elit, sed do eiusmod tempor incididunt ut labore et dolore magna aliqua. Ut enim ad minim veniam, quis nostrud exercitation ullamco laboris nisi ut aliquip ex ea commodo consequat.</div>
  <span class="qmark" style="left:366px;top:98px">“</span>
  <span class="qmark" style="left:730px;top:238px">”</span>
  <svg class="abs" style="left:803px;top:150px" width="24" height="30"><polygon points="0,0 24,15 0,30" fill="#fff"/></svg>
  <div class="avatar" role="img" aria-label="Customer portrait"></div>
  <div class="person"><b>Daniel Reyes</b><span>City Location</span></div>
</section>

<!-- newsletter & footer -->
<footer class="section footer">
  <div class="abs" role="img" aria-label="Dark photo of a business meeting with a world map overlay" style="inset:0;background:radial-gradient(ellipse at 70% 40%,rgba(90,95,105,.35),transparent 60%)"></div>
  <h2 class="news-title">NEWSLETTER SIGN UP</h2>
  <form class="news-form">
    <svg class="abs" style="left:25px;top:26px" width="22" height="17"><rect x="1" y="1" width="20" height="15" fill="#e6e6e6"/><polyline points="1,1 11,9 21,1" fill="none" stroke="#777" stroke-width="1.5"/></svg>
    <span class="news-input">Your Mail</span>
    <a class="btn subscribe">SUBSCRIBE</a>
  </form>

  <div class="col" style="left:50px"><h4>Important Links</h4>
    <ul><li>Affiliate Program</li><li>Special Promotions</li><li>Newsletter</li><li>Contact</li></ul></div>
  <div class="col" style="left:331px"><h4>Categories</h4>
    <ul><li>Webmail Login</li><li>Account Login</li><li>FAQs</li><li>Server References</li></ul></div>
  <div class="col" style="left:614px"><h4>Navigation</h4>
    <ul><li>About Us</li><li>Services</li><li>Tips</li><li>News</li><li>Contact Us</li></ul></div>
  <div class="col contact" style="left:866px;width:300px"><h4>Contact Us</h4>
    <ul>
      <li><svg width="12" height="16"><path d="M6 0a6 6 0 0 1 6 6c0 4-6 10-6 10S0 10 0 6a6 6 0 0 1 6-6z" fill="#e0e0e0"/><circle cx="6" cy="6" r="2.2" fill="#222"/></svg><span>Address Line1, Address Line-2<br>Lorem ipsum dolor<br>Country : 123456</span></li>
      <li><svg width="12" height="14"><rect x="2" y="0" width="8" height="14" rx="2" fill="#e0e0e0"/></svg><span>Office: 555.210.384</span></li>
      <li><svg width="12" height="14"><rect x="0" y="3" width="12" height="9" fill="#e0e0e0"/></svg><span>Fax: 555.210.384</span></li>
      <li><svg width="12" height="14"><rect x="0" y="3" width="12" height="9" fill="#e0e0e0"/><polyline points="0,3 6,8 12,3" fill="none" stroke="#222"/></svg><span>info@korbalex.com</span></li>
    </ul></div>

  <div class="bottom"></div>
  <p class="copy">Copyright 2016 Company Name. All Rights Reserved.</p>
  <div class="social"><span class="first"></span><span></span><span></span><span></span><span></span></div>
</footer>

</body>
</html>
```